I need a business card for ALVA Holdings. We are a young startup based in New Zealand working in internet marketing and web development. The design should have some element connected to New Zealand, such as wave, koru or silver fern, just don't use a kiwi bird.

```html
<!DOCTYPE html>
<html lang="en">
<head>
<meta charset="utf-8">
<title>ALVA Holdings – Business Card</title>
<link rel="stylesheet" href="https://fonts.googleapis.com/css2?family=Open+Sans:wght@400;600;700&display=swap">
<style>
  :root {
    --bg: #3a3d40;
    --card: #ffffff;
    --brand-blue: #0b6fbd;
    --wave-light: #cfe3f4;
    --text-dark: #3b3b3b;
    --text-white: #ffffff;
  }
  * { box-sizing: border-box; margin: 0; padding: 0; }
  html, body { width: 1200px; height: 1000px; overflow: hidden; }
  body {
    background: var(--bg);
    font-family: "Open Sans", sans-serif;
    color: var(--text-dark);
    position: relative;
  }
  .card {
    position: absolute;
    left: 250px;
    width: 700px;
    height: 400px;
    background: var(--card);
    overflow: hidden;
  }
  .card--back { top: 50px; }
  .card--front { top: 520px; }

  /* Back */
  .back-mark {
    position: absolute;
    left: 0; right: 0; top: 52px;
    display: flex; flex-direction: column; align-items: center; gap: 14px;
  }
  .back-mark__dot {
    width: 170px; height: 170px; border-radius: 50%;
    background: var(--brand-blue);
  }
  .back-mark__name {
    font-size: 30px; font-weight: 700; color: var(--brand-blue); line-height: 1.1;
  }
  .back-web {
    position: absolute; left: 0; right: 0; top: 340px;
    text-align: center; font-size: 20px; letter-spacing: 4px;
    color: var(--text-dark);
  }

  /* Front */
  .brand-name {
    position: absolute; left: 36px; top: 40px;
    font-size: 44px; font-weight: 700; color: var(--brand-blue);
    line-height: 1;
  }
  .title-band {
    position: absolute; left: 320px; right: 0; top: 100px; height: 66px;
    color: var(--text-white);
  }
  .title-band__wave {
    position: absolute; inset: 0; width: 100%; height: 100%;
  }
  .title-band__text {
    position: relative; text-align: right; padding: 8px 30px 0 0;
  }
  .title-band__name { font-size: 22px; font-weight: 700; line-height: 1.15; }
  .title-band__role { font-size: 17px; font-weight: 400; line-height: 1.15; }

  .contact-list {
    position: absolute; left: 36px; top: 222px;
    list-style: none; font-size: 18px; line-height: 25px;
  }
  .contact-list li { display: flex; align-items: center; gap: 8px; }
  .contact-list svg { width: 16px; height: 16px; fill: var(--brand-blue); flex: none; }

  .address {
    position: absolute; right: 36px; top: 284px;
    font-style: normal; font-size: 20px; line-height: 27px; text-align: left;
  }
</style>
</head>
<body>

<section class="card card--back" aria-label="Card back">
  <div class="back-mark">
    <div class="back-mark__dot"></div>
    <div class="back-mark__name">ALVA Holdings</div>
  </div>
  <p class="back-web">alvaholdings.com</p>
</section>

<section class="card card--front" aria-label="Card front">
  <div class="brand-name">ALVA Holdings</div>

  <div class="title-band">
    <svg class="title-band__wave" viewBox="0 0 380 66" preserveAspectRatio="none" aria-hidden="true">
      <path d="M0 66 C18 56 10 30 26 16 C36 7 44 0 56 0 H380 V66 Z" fill="var(--wave-light)"/>
      <path d="M18 66 C34 56 28 32 42 18 C52 8 60 0 72 0 H380 V66 Z" fill="var(--brand-blue)"/>
    </svg>
    <div class="title-band__text">
      <div class="title-band__name">MARA QUILL</div>
      <div class="title-band__role">PRESIDENT</div>
    </div>
  </div>

  <ul class="contact-list">
    <li>
      <svg viewBox="0 0 16 16" aria-hidden="true"><path d="M2 5c0-2 2-3 6-3s6 1 6 3v1h-3V5H5v1H2z M4 7h8l2 6H2z"/></svg>
      021 555 0142
    </li>
    <li>
      <svg viewBox="0 0 16 16" aria-hidden="true"><path d="M4 1h8v14H4z M5.5 3v9h5V3z" fill-rule="evenodd"/></svg>
      022 555 0187
    </li>
    <li>
      <svg viewBox="0 0 16 16" aria-hidden="true"><path d="M1 3h14v10H1z M2 4l6 5 6-5z" fill-rule="evenodd"/></svg>
      mara@alvaholdings.com
    </li>
  </ul>

  <address class="address">
    24 Harbour View Road<br>
    Westhaven, Auckland 1010<br>
    www.alvaholdings.com
  </address>
</section>

</body>
</html>
```